Re-Brand of TindelMox along with a new website design

TindelMox Ltd are a software & database development company using technologies such as PHP, C#, HTML, JQuery, Flex, AS3, MySQL, Oracle, MSSQL. We like to target all types of business from small to large.

We are great at coding but rubbish at design so thats where we need your help!

We want a complete re-brand of TindelMox including logo, website design, and business cards.

We would like a design that is clean but other than that, please feel free to be creative.

****Logo****
We are looking for a logo that appears professional but with a splash of colour that indicates a creative side. Please see below some logos that we like the look of:

We like this one because it has a nice simple and clear font for the name of the company but also an icon which is colourful and stands out. http://markvault.example/2013/03/brivelo/

We like this one because it is very clean, simple and again very clear. http://markvault.example/2013/03/quantorels/

http://markvault.example/2013/03/tide-lamp/
http://markvault.example/2013/02/velmorin/
http://markvault.example/2013/01/art-gallery-tarnwick/

As you will see from all of these examples, the font is very clear but there is always a graphic representing the company too. This is what we like.

****Website****
These are some of the examples of websites we like:
https://www.zestrune.example/
https://www.chatterlane.example/home
http://www.haldenimagery.example/
http://www.vistor.example/
http://quillbay.example/
https://www.usebriefnest.example/personal-intros
http://www.marmotpanel.example/

The current site can be found at tindelmox.example.uk

Reason: We have extended the deadline of the project by 5 days as I realise the original deadline was very tight.

Software

Requirements
Must have
• Website must have the following pages
Home
Services
Projects
About Us
Contact Us

```html
<!DOCTYPE html>
<html lang="en">
<head>
<meta charset="utf-8">
<title>TindelMox – Web, software, IT services</title>
<link href="https://fonts.googleapis.com/css2?family=Ubuntu:wght@400;500;700&display=swap" rel="stylesheet">
<style>
:root{
  --navy:#1b4fa0;
  --cyan:#14a5d6;
  --text:#333;
  --muted:#777;
  --header-top:#4fb0cf;
  --header-bottom:#a9dbea;
  --hero-top:#d5eef6;
  --hero-bottom:#ffffff;
  --section-bg:#f4f5f6;
  --card-border:#dde3e7;
  --footer-top:#0c4f68;
  --footer-bottom:#073045;
  --footer-text:#ffffff;
  --footer-muted:#7aa3b4;
}
*{margin:0;padding:0;box-sizing:border-box}
html,body{width:1200px;height:1088px;overflow:hidden}
body{font-family:"Ubuntu",sans-serif;color:var(--text);position:relative;background:#fff}
.abs{position:absolute}

.site-header{position:absolute;left:0;top:0;width:1200px;height:110px;
  background:linear-gradient(180deg,var(--header-top),var(--header-bottom));border-bottom:1px solid #c6e6f0}
.brand{position:absolute;left:131px;top:36px;display:flex;align-items:center;gap:10px}
.brand-mark{width:32px;height:32px;background:var(--cyan);border-radius:4px}
.brand-name{font-size:30px;font-weight:700;color:var(--cyan)}
.main-nav a{position:absolute;top:46px;font-size:12px;font-weight:700;color:#fff;text-decoration:none;transform:translateX(-50%);letter-spacing:.2px}
.main-nav a.active{top:39px;background:linear-gradient(#33a8e6,#2450c7);padding:6px 9px;border-radius:4px;box-shadow:0 2px 4px rgba(0,0,0,.25)}
.main-nav a.active::after{content:"";position:absolute;left:50%;bottom:-5px;margin-left:-5px;border:5px solid transparent;border-bottom:0;border-top-color:#2450c7}

.hero{position:absolute;left:0;top:110px;width:1200px;height:396px;
  background:linear-gradient(180deg,var(--hero-top),var(--hero-bottom) 70%);border-bottom:1px solid #9aa}
.hero h1{position:absolute;left:131px;top:42px;font-size:38px;font-weight:700;color:var(--navy)}
.hero h1 span{color:var(--cyan)}
.hero .tagline{position:absolute;left:131px;top:88px;font-size:17px;color:var(--cyan)}
.hero .intro{position:absolute;left:131px;top:145px;width:495px;font-size:12px;line-height:19.7px;color:var(--text)}
.hero .intro p+p{margin-top:19.7px}
.btn{display:inline-block;border:1px solid #c8d3da;border-radius:18px;background:linear-gradient(#fff,#e8eef2);
  color:var(--navy);font-weight:500;text-decoration:none;text-align:center;box-shadow:0 2px 2px rgba(0,0,0,.12)}
.hero .btn{position:absolute;left:131px;top:305px;width:180px;height:33px;line-height:31px;font-size:14.5px}
.hero-rule{position:absolute;left:320px;top:322px;width:750px;height:1px;background:linear-gradient(90deg,#e3eef2,transparent)}
.devices{position:absolute;left:675px;top:68px;width:347px;height:197px;border-radius:10px;
  background:radial-gradient(ellipse at 50% 45%,#5d9fd6,#2f5f8c 55%,#cfe6f1 100%)}
.dots{position:absolute;left:560px;top:358px;display:flex;gap:15px;align-items:center}
.dots i{width:7px;height:7px;border-radius:50%;background:#d4dadd;display:block}
.dots i.on{width:10px;height:10px;background:var(--cyan)}

.services{position:absolute;left:0;top:507px;width:1200px;height:416px;background:var(--section-bg)}
.services h2{position:absolute;left:131px;top:18px;font-size:29px;font-weight:400;color:var(--cyan)}
.services .all{position:absolute;left:929px;top:22px;width:139px;height:26px;line-height:24px;font-size:13.5px;color:var(--muted);font-weight:400;border-radius:14px}
.arrow{position:absolute;top:218px}
.card{position:absolute;top:71px;width:176px;height:320px;background:linear-gradient(#fff,#f3f7f9);
  border:1px solid var(--card-border);border-radius:3px;box-shadow:0 1px 3px rgba(0,0,0,.1)}
.card svg.icon{position:absolute;left:50%;top:18px;margin-left:-38px}
.card h3{position:absolute;left:0;top:96px;width:100%;text-align:center;font-size:17px;line-height:20px;font-weight:500;color:var(--cyan)}
.card p{position:absolute;left:17px;width:142px;font-size:11.3px;line-height:18px;color:var(--text)}
.card hr{position:absolute;left:17px;top:255px;width:142px;border:0;border-top:1px solid #dcdfe1}
.card .btn{position:absolute;left:17px;top:274px;width:141px;height:29px;line-height:27px;font-size:12.5px}

.site-footer{position:absolute;left:0;top:923px;width:1200px;height:165px;
  background:linear-gradient(var(--footer-top),var(--footer-bottom));border-top:2px solid #062a3a}
.foot-nav{position:absolute;left:131px;top:31px;display:flex;gap:20px}
.foot-nav a{font-size:11px;font-weight:700;color:var(--footer-text);text-decoration:none}
.copy{position:absolute;left:131px;top:75px;font-size:11.5px;color:var(--footer-muted)}
.vline{position:absolute;top:35px;width:1px;height:110px;background:rgba(255,255,255,.12)}
.foot-label{position:absolute;top:31px;font-size:10.5px;font-weight:700;color:#a9c3cf}
.contact h4{position:absolute;left:677px;top:64px;font-size:17.5px;font-weight:500;color:#fff}
.contact .phone{position:absolute;left:675px;top:91px;font-size:23px;font-weight:500;color:#1cb2e4}
.contact .mail{position:absolute;left:675px;top:117px;font-size:15px;color:#1cb2e4}
.social{position:absolute;left:919px;top:68px;display:flex;gap:15px}
.social span{width:40px;height:24px;border-radius:12px;background:linear-gradient(#fff,#dfe7ec)}
.top-link{position:absolute;left:919px;top:121px;font-size:10.5px;font-weight:700;color:var(--footer-muted)}
</style>
</head>
<body>

<header class="site-header">
  <div class="brand"><span class="brand-mark"></span><span class="brand-name">TindelMox</span></div>
  <nav class="main-nav">
    <a class="active" href="#" style="left:457px">HOME</a>
    <a href="#" style="left:584px">SERVICES</a>
    <a href="#" style="left:722px">PROJECTS</a>
    <a href="#" style="left:862px">ABOUT US</a>
    <a href="#" style="left:1012px">CONTACT US</a>
  </nav>
</header>

<section class="hero">
  <h1>Welcome to <span>TindelMox</span></h1>
  <div class="tagline">Web, software, IT services</div>
  <div class="intro">
    <p>If you are looking for web, software, or IT services that really deliver but you don't want to pay over the odds then TindelMox is the right team for you.</p>
    <p>Based in Harrowby our clients are both local, national, both large and small. You may be a start-up business in need of a 'get me up and running quickly' website, or a multi-million pound brand looking for an all singing, all dancing bespoke app.</p>
  </div>
  <div class="hero-rule"></div>
  <a class="btn" href="#">Read more about us</a>
  <div class="devices" role="img" aria-label="Laptop, tablet and smartphone showing app screens"></div>
  <div class="dots"><i></i><i class="on"></i><i></i><i></i></div>
</section>

<section class="services">
  <h2>Our services</h2>
  <a class="btn all" href="#">View all services</a>

  <svg class="arrow" style="left:168px" width="16" height="30" viewBox="0 0 16 30"><path d="M14 1 2 15l12 14" fill="none" stroke="#14a5d6" stroke-width="1.6"/></svg>
  <svg class="arrow" style="left:1016px" width="16" height="30" viewBox="0 0 16 30"><path d="M2 1l12 14L2 29" fill="none" stroke="#14a5d6" stroke-width="1.6"/></svg>

  <defs></defs>
  <article class="card" style="left:221px">
    <svg class="icon" width="76" height="64" viewBox="0 0 76 64">
      <defs><linearGradient id="g1" x1="0" y1="0" x2="0" y2="1"><stop offset="0" stop-color="#1ab0e4"/><stop offset="1" stop-color="#2a36b8"/></linearGradient></defs>
      <rect x="8" y="2" width="60" height="44" rx="3" fill="url(#g1)"/>
      <rect x="13" y="7" width="50" height="34" fill="#fff"/>
      <path d="M2 50h72l-4 8H6z" fill="url(#g1)"/>
      <path d="M28 15l10 14 2-6 6-1z" fill="#2a36b8"/>
    </svg>
    <h3>Website Design<br>&amp; Development</h3>
    <p style="top:154px">Your website is a representa-tion of who you are or what your business stands for.</p>
    <hr><a class="btn" href="#">Read more</a>
  </article>

  <article class="card" style="left:415px">
    <svg class="icon" width="76" height="64" viewBox="0 0 76 64">
      <defs><linearGradient id="g2" x1="0" y1="0" x2="0" y2="1"><stop offset="0" stop-color="#1ab0e4"/><stop offset="1" stop-color="#2a36b8"/></linearGradient></defs>
      <rect x="8" y="2" width="60" height="44" rx="3" fill="url(#g2)"/>
      <rect x="13" y="7" width="50" height="34" fill="#fff"/>
      <path d="M2 50h72l-4 8H6z" fill="url(#g2)"/>
      <rect x="20" y="28" width="8" height="9" fill="#2a36b8"/><rect x="32" y="22" width="8" height="15" fill="#2a36b8"/><rect x="44" y="14" width="8" height="23" fill="#2a36b8"/>
    </svg>
    <h3>Rich Internet<br>Applications</h3>
    <p style="top:154px">You may be asking yourself, “what the heck is a Rich Internet Application..?” The chances are you play with one every day.</p>
    <hr><a class="btn" href="#">Read more</a>
  </article>

  <article class="card" style="left:609px">
    <svg class="icon" width="76" height="64" viewBox="0 0 76 64">
      <defs><linearGradient id="g3" x1="0" y1="0" x2="0" y2="1"><stop offset="0" stop-color="#1ab0e4"/><stop offset="1" stop-color="#2a36b8"/></linearGradient></defs>
      <rect x="17" y="0" width="42" height="62" rx="5" fill="url(#g3)"/>
      <rect x="22" y="6" width="32" height="45" rx="2" fill="#fff"/>
      <rect x="33" y="55" width="10" height="2.5" rx="1" fill="#fff"/>
    </svg>
    <h3>Mobile &amp; Tablet<br>Applications</h3>
    <p style="top:154px">If you are sitting on the next great idea for a mobile or tablet app TindelMox has all the experience you need.</p>
    <hr><a class="btn" href="#">Read more</a>
  </article>

  <article class="card" style="left:803px">
    <svg class="icon" width="76" height="64" viewBox="0 0 76 64">
      <rect x="26" y="0" width="24" height="24" fill="#1ab0e4"/>
      <path d="M38 24v14M16 38h44M16 38v10M38 38v10M60 38v10" stroke="#2a36b8" stroke-width="2.5" fill="none"/>
      <rect x="9" y="48" width="14" height="13" rx="2" fill="#2a36b8"/><rect x="31" y="48" width="14" height="13" rx="2" fill="#2a36b8"/><rect x="53" y="48" width="14" height="13" rx="2" fill="#2a36b8"/>
    </svg>
    <h3>Enterprise<br>Development</h3>
    <p style="top:160px">You may be familiar with the usual clunky enterprise systems you probably have a very poor opinion of them.</p>
    <hr><a class="btn" href="#">Read more</a>
  </article>
</section>

<footer class="site-footer">
  <nav class="foot-nav">
    <a href="#">HOME</a><a href="#">SERVICES</a><a href="#">PROJECTS</a><a href="#">ABOUT US</a><a href="#">CONTACT US</a>
  </nav>
  <div class="copy">© Copyright 2013 tindelmox.example.uk. All rights reserved.</div>
  <div class="vline" style="left:653px"></div>
  <div class="vline" style="left:895px"></div>
  <div class="foot-label" style="left:677px">DO YOU HAVE ANY QUESTIONS?</div>
  <div class="contact">
    <h4>Contact Us</h4>
    <div class="phone">01632 960 418</div>
    <div class="mail">contact@tindelmox.example.uk</div>
  </div>
  <div class="foot-label" style="left:919px">SOCIAL NETWORKS</div>
  <div class="social"><span></span><span></span><span></span></div>
  <div class="top-link">BACK TO TOP &#9652;</div>
</footer>

</body>
</html>
```